Heritage Hollow Business Cards

Require a business card design. <br/><br/>Needs to include logo (either round or long version) plus these details:<br/>Maya Torvel<br/>Heritage Hollow<br/>maya@quonbrook.com.au<br/>02 6481 7390<br/>PO Box Glenwarra NSW 2913<br/>www.heritagehollow.com.au<br/><br/>I need in an editable format so that I can create for multiple staff members. <br/><br/>

Target Market(s)

We are an online store selling renovation products to home owners are builders. Looking for a classic classy design.

Industry/Entity Type

Home And Garden

Contact Information for Business Card

Maya Torvel
Heritage Hollow
maya@quonbrook.com.au
02 6481 7390
PO Box Glenwarra NSW 2913
www.heritagehollow.com.au

Colors

Designer to choose colors to be used in the design.

Requirements
Must have
• Must include Logo.

```html
<!DOCTYPE html>
<html lang="en">
<head>
<meta charset="UTF-8">
<title>Heritage Hollow Business Cards</title>
<link href="https://fonts.googleapis.com/css2?family=Lato:wght@400;700&display=swap" rel="stylesheet">
<style>
  :root {
    --page-bg: #f0f0f0;
    --card-black: #020402;
    --rain-green: #0d3a12;
    --brand-green: #1f8a2a;
    --ink-white: #ffffff;
    --ink-soft: #dcdcdc;
  }
  * { margin: 0; padding: 0; box-sizing: border-box; }
  html, body {
    width: 1200px; height: 1000px; overflow: hidden;
    background: var(--page-bg);
    font-family: "Lato", sans-serif;
  }
  .card {
    position: absolute;
    left: 341px; width: 515px;
    overflow: hidden;
    background: var(--card-black);
  }
  .card--front { top: 144px; height: 356px; }
  .card--back { top: 539px; height: 346px; }
  .card__texture {
    position: absolute; inset: 0;
    background:
      radial-gradient(ellipse at 50% 50%, rgba(0,0,0,0) 30%, rgba(0,0,0,0.55) 100%),
      linear-gradient(180deg, var(--rain-green) 0%, var(--card-black) 45%, var(--rain-green) 100%);
    opacity: 0.7;
  }
  .front-logo {
    position: absolute; left: 96px; top: 120px;
    display: flex; align-items: center; gap: 14px;
  }
  .front-logo__mark {
    width: 58px; height: 58px; border-radius: 50%;
    border: 2px solid var(--brand-green);
  }
  .front-logo__name {
    font-size: 36px; font-weight: 400; color: var(--brand-green);
    letter-spacing: 0.5px;
  }
  .back-logo {
    position: absolute; left: 44px; top: 45px;
    display: flex; align-items: flex-end; gap: 8px;
  }
  .back-logo__mark {
    width: 52px; height: 52px; border-radius: 50%;
    border: 1px solid var(--ink-soft);
  }
  .back-logo__name {
    font-size: 22px; color: var(--ink-soft); line-height: 1; padding-bottom: 2px;
  }
  .back-url {
    position: absolute; left: 58px; top: 106px;
    font-size: 14px; color: var(--ink-soft);
  }
  .staff-name {
    position: absolute; left: 59px; top: 143px;
    font-size: 27px; color: var(--ink-white);
  }
  .contact-list {
    position: absolute; left: 62px; top: 197px;
    list-style: none;
  }
  .contact-list li {
    display: flex; align-items: center; gap: 8px;
    height: 35px;
    font-size: 22px; color: var(--ink-white);
  }
  .contact-list svg { width: 27px; height: 27px; flex: none; }
</style>
</head>
<body>
  <section class="card card--front">
    <div class="card__texture" role="img" aria-label="Dark green digital rain background pattern"></div>
    <div class="front-logo">
      <span class="front-logo__mark"></span>
      <span class="front-logo__name">Heritage Hollow</span>
    </div>
  </section>

  <section class="card card--back">
    <div class="card__texture" role="img" aria-label="Dark green digital rain background pattern"></div>
    <div class="back-logo">
      <span class="back-logo__mark"></span>
      <span class="back-logo__name">Heritage Hollow</span>
    </div>
    <p class="back-url">heritagehollow.com.au</p>
    <h1 class="staff-name" style="font-weight:400">Maya Torvel</h1>
    <ul class="contact-list">
      <li>
        <svg viewBox="0 0 28 28" aria-hidden="true">
          <circle cx="14" cy="14" r="12.5" fill="none" stroke="#fff" stroke-width="2"/>
          <rect x="7" y="9" width="14" height="10" fill="#fff"/>
          <polyline points="7,9 14,15 21,9" fill="none" stroke="#020402" stroke-width="1.3"/>
        </svg>
        maya@quonbrook.com.au
      </li>
      <li>
        <svg viewBox="0 0 28 28" aria-hidden="true">
          <circle cx="14" cy="14" r="12.5" fill="none" stroke="#fff" stroke-width="2"/>
          <path d="M9 8 q-2 2 0 6 q3 5 8 7 q3 1 4-1 l-3-3 l-2 1 q-3-2-4-5 l1-2 z" fill="#fff"/>
        </svg>
        02 6481 7390
      </li>
      <li>
        <svg viewBox="0 0 28 28" aria-hidden="true">
          <circle cx="14" cy="14" r="12.5" fill="none" stroke="#fff" stroke-width="2"/>
          <path d="M14 6 L22 13 H19.5 V21 H16 V16 H12 V21 H8.5 V13 H6 Z" fill="#fff"/>
        </svg>
        PO Box Glenwarra NSW 2913
      </li>
    </ul>
  </section>
</body>
</html>
```